HTML Web layout / data visualization for an information software application

We have a product used by patent analysts to allow them examine information stored in patents - particularly those patents that include biological sequences like DNA, RNA, and protein.

When the user opens up a particular patent, they currently see a very poorly organized wall of text, presenting fields of data to them in unorganized ways. We have attached screenshots of the current interface.

The project is to redesign that layout so that the same information is presented in a way which is brings important data to the the eyes of the user, categorizes data appropriately, and is visually appealing. We have proposed logical categorizations of data in the document called "Fields documentation."

The deliverable should be an HTML5 file that renders one or more of the examples of records we've provided in your new design.

Description of files:

"Examples of records badly displayed": MS Word file that shows three different examples of the records we would like to better visualize.

"screengrab1.tiff" and "screengrab2.tiff": pictures of how these records sit inside of our product. This is presented to give you a sense of screen real estate, our look and feel, and colors. We do not want the whole screen redesigned - just the record display itself.

"Fields documentation": detailed documentation of what each field means. We have tried to group them logically for you, and have also attempted to inform you as to which fields are linked to others.

Hi all,

Thanks for the designs so far. Unfortunately, nearly every design fails to understand the nature of the project. The problem we have is not about fonts and colors (although those matter). It is about grouping information together and displaying data in a way that provides insight. In the original brief, we say:

The document we have uploaded called "Fields documentation" is the most important document. We sense that very few of you have taken it into account. It provides notes on the nature of the data in the report and gives signs of the ways in which a creative designer might help to arrange the content.

Thanks for your consideration of this project.

TM

Target Market(s)

Patent analysts, heavily educated scientists, Ph.Ds.

Industry/Entity Type

Software

```html
<!DOCTYPE html>
<html lang="en">
<head>
<meta charset="utf-8">
<title>Sequence Hit – Subject Annotation</title>
<link href="https://fonts.googleapis.com/css2?family=Noto+Sans:wght@400;700&display=swap" rel="stylesheet">
<style>
:root{
  --page-bg:#cde8f4;
  --header-bg:#08679b;
  --header-line:#3b8bb8;
  --row-bg:#dcf0f9;
  --row-line:#b6d9ea;
  --panel-bg:#ffffff;
  --panel-line:#a9d2e5;
  --menu-bg:#c1e3f2;
  --menu-active:#0a6699;
  --ink:#1c1c1c;
  --title-ink:#16415e;
  --link:#0b5e8e;
  --close:#2a72b5;
  --tab-bg:#eef6fa;
  --tab-line:#a7c9da;
  --field-bg:#efefef;
  --frame:#a8a8a8;
}
*{box-sizing:border-box;margin:0;padding:0}
html,body{width:1200px;height:661px;overflow:hidden}
body{background:var(--page-bg);font-family:"Noto Sans",Verdana,sans-serif;color:var(--ink);position:relative}

.hits-header{position:absolute;left:0;top:0;width:1200px;height:52px;background:var(--header-bg);display:flex}
.hits-header .col{height:100%;border-right:1px solid var(--header-line);display:flex;align-items:flex-start;justify-content:center;text-align:center;padding-top:9px;font-size:13px;line-height:16px;color:#fff}
.hits-header .c-check{flex-direction:column;align-items:center;gap:4px;padding-top:9px}
.hit-row .col{height:100%;border-right:1px solid var(--row-line);display:flex;align-items:center;font-size:12.5px;line-height:17px;color:var(--ink)}
.c-check{width:48px}
.c-qid{width:73px}.c-sid{width:69px}.c-aid{width:67px}.c-eval{width:87px}
.c-query1{width:96px}.c-query2{width:98px}.c-ident{width:193px}.c-desc{flex:1;border-right:none!important}
.hit-row{position:absolute;left:0;top:52px;width:1200px;height:51px;background:var(--row-bg);display:flex;border-bottom:1px solid var(--row-line)}
.hit-row .c-check{justify-content:center}
.hit-row .num{justify-content:flex-end;padding-right:7px}
.hit-row .txt{justify-content:flex-start;padding-left:7px;text-align:left}
.hit-row .c-desc{padding-left:7px;padding-right:60px}
.box{width:15px;height:15px;background:#fff;border:1px solid #7a9fb3;border-radius:2px}
.sort-btn{width:15px;height:13px;background:#fff;border:1px solid #7a9fb3;display:flex;align-items:center;justify-content:center}

.close-link{position:absolute;right:12px;font-size:12.5px;color:var(--close)}
.close-top{top:110px}.close-bottom{top:632px}

.tabs{position:absolute;left:10px;top:136px;display:flex;gap:4px}
.tab{height:28px;padding:0 9px;background:var(--tab-bg);border:1px solid var(--tab-line);border-bottom:none;font-size:13px;line-height:28px;color:#333}
.tab.active{background:#fff;height:31px;margin-top:-3px;line-height:32px;color:#111}

.panel{position:absolute;left:10px;top:164px;width:1180px;height:460px;background:var(--panel-bg);border:1px solid var(--panel-line)}
.field-menu{position:absolute;left:12px;top:15px;width:182px;list-style:none}
.field-menu li{height:26.5px;margin-bottom:1.3px;background:var(--menu-bg);font-size:13.5px;line-height:26.5px;padding-left:14px;color:#1d2e38}
.field-menu li.active{background:var(--menu-active);color:#fff;font-weight:700;position:relative}
.cursor{position:absolute;left:134px;top:6px}

.record-title{position:absolute;left:214px;top:12px;font-size:16.5px;line-height:22px;font-weight:700;color:var(--title-ink);letter-spacing:.3px;white-space:nowrap}
.date-table{position:absolute;left:214px;top:40px;width:963px;border:5px solid var(--frame);border-collapse:collapse;background:#fff}
.date-table td{height:30px;font-size:13.5px;border-bottom:2px solid #d4d4d4}
.date-table tr:last-child td{border-bottom:none}
.date-table .label{width:209px;background:var(--field-bg);padding-left:14px;color:#222}
.date-table .value{padding-left:18px;color:var(--link)}
</style>
</head>
<body>

<div class="hits-header">
  <div class="col c-check"><span class="sort-btn"><svg width="9" height="7" viewBox="0 0 9 7"><path d="M0 0h9L4.5 7z" fill="#08679b"/></svg></span><span class="box"></span></div>
  <div class="col c-qid">Query<br>% Id</div>
  <div class="col c-sid">Subj. %<br>Id</div>
  <div class="col c-aid">Align %<br>Id</div>
  <div class="col c-eval">E-val</div>
  <div class="col c-query1">Query<br>Identifier</div>
  <div class="col c-query2">Query<br>Identifier</div>
  <div class="col c-ident">Identifier</div>
  <div class="col c-desc">Description / Title</div>
</div>

<div class="hit-row">
  <div class="col c-check"><span class="box"></span></div>
  <div class="col c-qid num">98.9</div>
  <div class="col c-sid num">9.03</div>
  <div class="col c-aid num">99.72</div>
  <div class="col c-eval num">8.90e-216</div>
  <div class="col c-query1 txt">seq_1</div>
  <div class="col c-query2 txt">seq_1</div>
  <div class="col c-ident txt">EP2539456-0043</div>
  <div class="col c-desc txt">INCREASING PLANT GROWTH BY MODULATING OMEGA-AMIDASE EXPRESSION IN PLANTS</div>
</div>

<span class="close-link close-top">[close]</span>

<div class="tabs">
  <div class="tab">Alignment</div>
  <div class="tab active">Subject Annotation</div>
  <div class="tab">Subject Sequence</div>
  <div class="tab">Query Sequence</div>
</div>

<section class="panel">
  <ul class="field-menu">
    <li>Identifier</li>
    <li>Patent</li>
    <li>Organism</li>
    <li>Feature Table</li>
    <li>PCT pub. date</li>
    <li>Priority</li>
    <li>Applicatin number</li>
    <li>Number of SEQ</li>
    <li>Equivalents</li>
    <li class="active">Date
      <svg class="cursor" width="24" height="28" viewBox="0 0 24 28"><path d="M7 2a2 2 0 0 1 4 0v9l1-.5a2 2 0 0 1 3 1.3 2 2 0 0 1 3 1.2 2 2 0 0 1 3 1.5V21c0 3-2 5-5 5h-5c-2 0-3-1-4-2l-5-6a2 2 0 0 1 3-2.6L7 17z" fill="#fff" stroke="#111" stroke-width="1.3" stroke-linejoin="round"/></svg>
    </li>
    <li>Legal</li>
    <li>Comments</li>
    <li>Subj.</li>
    <li>Description</li>
    <li>Link out</li>
  </ul>

  <h2 class="record-title">INCREASING PLANT GROWTH BY MODULATING OMEGA-AMIDASE EXPRESSION IN PLANTS</h2>
  <table class="date-table">
    <tr><td class="label">Publication date</td><td class="value">02-Jan-2013</td></tr>
    <tr><td class="label">Date of entry</td><td class="value">07-Feb-2013</td></tr>
    <tr><td class="label">Patent filing date</td><td class="value">28-Feb-2011</td></tr>
    <tr><td class="label">Earliest priority date</td><td class="value">28-Feb-2010</td></tr>
    <tr><td class="label">Earliest pub. date</td><td class="value">02-Jan-2013</td></tr>
  </table>
</section>

<span class="close-link close-bottom">[close]</span>

</body>
</html>
```